US company marketing to law enforcement needs brochure design

We have created a new logo and now need to update our printed material. What we really need is a "style" or "template" for how our brochures will look in the future. Enclosed is the brochure draft with the old style and logo. Also enclosed is the new logo. As we are marketing to US law enforcement it is important the the brochure design is strong, powerful and that we are looking experienced and trustworthy. However, we also want to look modern in line with the logo update.

Target Market(s)

Law enforcement

Industry/Entity Type

Marketing

```html
<!DOCTYPE html>
<html lang="en">
<head>
<meta charset="utf-8">
<title>Meridian Reform – Brochure</title>
<link href="https://fonts.googleapis.com/css2?family=Barlow:wght@400;500;600;700&display=swap" rel="stylesheet">
<style>
  :root {
    --navy: #1f386c;
    --navy-deep: #1a3060;
    --blue: #2f6fb3;
    --grey-text: #6b6b6b;
    --grey-name: #8c8c8c;
    --paper: #ffffff;
    --backdrop: #ececec;
    --placeholder: #f6f6f6;
    --placeholder-line: #e2e2e2;
    --rule: rgba(255,255,255,0.22);
  }
  * { box-sizing: border-box; margin: 0; padding: 0; }
  html, body { width: 1200px; height: 1000px; overflow: hidden; }
  body { background: var(--backdrop); font-family: "Barlow", Arial, sans-serif; position: relative; }

  .brochure { position: absolute; left: 53px; top: 68px; width: 1074px; height: 759px; display: flex; }

  /* Left panel */
  .panel-intro { width: 491px; height: 100%; background: var(--paper); position: relative; }
  .brand { position: absolute; left: 42px; top: 42px; display: flex; align-items: center; gap: 20px; }
  .brand-mark { width: 65px; height: 65px; border-radius: 50%; background: var(--navy); }
  .brand-name { font-size: 36px; font-weight: 500; color: var(--grey-name); letter-spacing: -0.5px; }
  .photo-placeholder { position: absolute; left: 40px; top: 135px; width: 411px; height: 194px; }
  .features { position: absolute; left: 41px; top: 384px; display: grid; grid-template-columns: 221px 200px; row-gap: 52px; }
  .feature h2 { font-size: 17px; font-weight: 500; color: var(--navy); line-height: 21px; letter-spacing: 0.4px; text-transform: uppercase; margin-bottom: 13px; }
  .feature p { font-size: 9.6px; line-height: 12.8px; color: var(--grey-text); width: 190px; }

  /* Middle photo panel */
  .panel-photo { width: 302px; height: 100%;
    background:
      linear-gradient(90deg, transparent 0 48px, rgba(47,111,179,0.55) 48px 95px, transparent 95px 143px, rgba(47,111,179,0.6) 163px 186px, transparent 186px),
      linear-gradient(160deg, #d9dbe0 0%, #9ea4ae 30%, #3d5a8c 55%, #23407a 80%, #1d3566 100%); }

  /* Right panel */
  .panel-services { width: 281px; height: 100%; background: var(--navy); color: #fff; text-align: right; padding: 0 50px 0 0; position: relative; }
  .service-brand { position: absolute; right: 50px; top: 60px; display: flex; align-items: center; gap: 8px; }
  .service-brand-mark { width: 14px; height: 14px; border-radius: 50%; background: #fff; }
  .service-brand-name { font-size: 15px; font-weight: 700; color: #fff; }
  .service { position: absolute; right: 50px; width: 200px; }
  .service h3 { font-size: 17px; font-weight: 700; line-height: 21px; letter-spacing: 0.4px; text-transform: uppercase; margin-bottom: 6px; }
  .service ul { list-style: none; font-size: 10.6px; line-height: 13px; }
  .rule { position: absolute; right: 0; width: 205px; height: 1px; background: var(--rule); }
</style>
</head>
<body>
  <main class="brochure">
    <section class="panel-intro">
      <div class="brand">
        <div class="brand-mark"></div>
        <div class="brand-name">Meridian Reform</div>
      </div>
      <svg class="photo-placeholder" viewBox="0 0 411 194" role="img" aria-label="Image placeholder">
        <rect width="411" height="194" fill="var(--placeholder)"/>
        <line x1="0" y1="0" x2="411" y2="194" stroke="var(--placeholder-line)"/>
        <line x1="411" y1="0" x2="0" y2="194" stroke="var(--placeholder-line)"/>
      </svg>
      <div class="features">
        <article class="feature"><h2>Experienced<br>Professionals</h2><p>MeridianReform's core management and operations team has over 25+ years of exerience developing and administerating programs for prosecuters, courts and probation. Each program has unique requirements for the participants based on the goals of each jurisdiction.</p></article>
        <article class="feature"><h2>Experienced<br>Professionals</h2><p>MeridianReform's core management and operations team has over 25+ years of exerience developing and administerating programs for prosecuters, courts and probation. Each program has unique requirements for the participants based on the goals of each jurisdiction.</p></article>
        <article class="feature"><h2>Experienced<br>Professionals</h2><p>MeridianReform's core management and operations team has over 25+ years of exerience developing and administerating programs for prosecuters, courts and probation. Each program has unique requirements for the participants based on the goals of each jurisdiction.</p></article>
        <article class="feature"><h2>Experienced<br>Professionals</h2><p>MeridianReform's core management and operations team has over 25+ years of exerience developing and administerating programs for prosecuters, courts and probation. Each program has unique requirements for the participants based on the goals of each jurisdiction.</p></article>
      </div>
    </section>

    <section class="panel-photo" role="img" aria-label="Photograph of a glass office tower seen from below, tinted blue"></section>

    <section class="panel-services">
      <div class="service-brand"><div class="service-brand-mark"></div><div class="service-brand-name">Meridian Reform</div></div>

      <div class="service" style="top:133px">
        <h3>Custom<br>Solutions</h3>
        <ul><li>All offender programs are</li><li>customized to meet the unique</li><li>needs of your justificaton.</li></ul>
      </div>
      <div class="rule" style="top:235px"></div>

      <div class="service" style="top:252px">
        <h3>Full Menu of<br>Conditions</h3>
        <ul>
          <li>Case Management</li><li>Face to face meetings</li><li>Offender Education</li><li>Group Counselling</li><li>Fine and Fee Recovery</li><li>Victim Restitution Recovery</li><li>Interactive Journaling</li><li>Drug testing</li><li>Alcohol monitoring</li><li>Community Service</li><li>Community Resource Referrals</li><li>GPS monitoring</li><li>Home detention</li><li>Offender communication</li><li>Preparation of court paperwork</li><li>Reporting</li>
        </ul>
      </div>
      <div class="rule" style="top:525px"></div>

      <div class="service" style="top:548px">
        <h3>Comprehensive<br>Administrative<br>Services</h3>
        <ul>
          <li>Eligible case screening</li><li>Case referral</li><li>Data entry</li><li>Electronic case files</li><li>Offender communication</li><li>Reporting</li>
        </ul>
      </div>
    </section>
  </main>
</body>
</html>
```